Serial Entrepreneur Business Card: 4 Logo Design

I am a serial entrepreneur and a full time mechanical engineer. I have four businesses. I would like to display them all on one business card.
*Please see the attached PDF for the design requirements*

www.KelbroNest.com

Businesses
-KelbroNest
-Quiet Lantern Properties
-Torlen Products
-Drosk Harbor Cast

Target Market(s)

Clients, Entrepreneurs, Associates, really anyone. Should be very professional.

Industry/Entity Type

Entrepreneur

Contact Information for Business Card

3.5" x 2" Standard Business Card Size
** Please review the attached requirement PDF for in depth detail on what I am expecting**

Font styles to use
Sans Serif

Requirements
Must have
• My personal contact information:
• First Name: Dae hwan
• Last Name: Pellow
• Nick Name: Riko
• Address: 83 Tolmer Court, Brindlewick OR 97392
• Phone Number: 555-574-2916
• Email: RikodPellow@mailnest.example
• Website: www.KelbroNest.com
• All Four Logos of the Companies I own:
• -KelbroNest
• -Quiet Lantern Properties
• -Torlen Products
• -Drosk Harbor Cast
• My Professions:
• -Prototyping Engineer
• -Real Estate Investor
• -Financial Blogger
• -Video Podcaster
• -Online Retail Seller
Nice to have
• If it fits, please include the website for each logo, if there is more space please include the email for each.
• It might be nice to have the QX GUILD Logo, or TOVRA logo for my full-time job. But only if it fits.

```html
<!DOCTYPE html>
<html lang="en">
<head>
<meta charset="utf-8">
<title>Dae hwan Riko Pellow – Business Card</title>
<link rel="stylesheet" href="https://fonts.googleapis.com/css2?family=Roboto:ital,wght@0,400;0,500;0,700;1,700;1,900&display=swap">
<style>
  :root {
    --board: #7f8a87;
    --label: #e8eeed;
    --card: #ffffff;
    --tile: #e3e6e6;
    --ink: #161819;
    --slate: #5d686b;
    --green: #3a9e2e;
    --cyan: #72f1f6;
    --rule: #d5d9d9;
  }
  * { box-sizing: border-box; margin: 0; padding: 0; }
  html, body { width: 849px; height: 1200px; overflow: hidden; }
  body {
    background: var(--board);
    font-family: "Roboto", Arial, sans-serif;
    position: relative;
  }
  .side-label {
    position: absolute;
    left: 26px;
    font-size: 18px;
    letter-spacing: 1px;
    color: var(--label);
    font-weight: 400;
  }
  .side-label.front { top: 290px; }
  .side-label.back { top: 790px; }

  .card {
    position: absolute;
    left: 147px;
    width: 551px;
    height: 317px;
    border-radius: 44px;
    background: var(--card);
    overflow: hidden;
    box-shadow: 0 22px 18px -14px rgba(40, 48, 46, 0.45);
  }
  .card.front { top: 142px; }
  .card.back { top: 630px; }

  /* logo grid */
  .tile {
    position: absolute;
    display: flex;
    align-items: center;
    justify-content: center;
    text-align: center;
    font-weight: 700;
    line-height: 1.1;
    color: var(--ink);
  }
  .tile.shaded { background: var(--tile); }
  .tile .brand-dot {
    display: inline-block;
    width: 9px; height: 9px;
    border-radius: 50%;
    background: currentColor;
    margin-bottom: 5px;
  }
  .tile-inner { display: flex; flex-direction: column; align-items: center; }

  .front .grid-line-v {
    position: absolute; left: 159px; top: 0; width: 2px; height: 317px;
    background: linear-gradient(to right, #d9dcdc, #ffffff);
  }
  .front .grid-line-h {
    position: absolute; left: 0; top: 159px; width: 385px; height: 2px;
    background: linear-gradient(to right, #ffffff, #d9dcdc 40%, #ffffff);
  }
  .front .t-kelbro  { left: 28px;  top: 32px;  width: 131px; height: 128px; border-radius: 14px 0 0 0; font-size: 15px; }
  .front .t-cast    { left: 161px; top: 50px;  width: 108px; height: 110px; border-radius: 0 16px 0 0; font-size: 14px; }
  .front .t-lantern { left: 43px;  top: 161px; width: 116px; height: 119px; border-radius: 0 0 0 16px; font-size: 13px; }
  .front .t-torlen  { left: 161px; top: 161px; width: 128px; height: 133px; border-radius: 0 0 16px 0; font-size: 15px; }

  .identity {
    position: absolute;
    left: 320px;
    top: 62px;
    color: var(--slate);
  }
  .identity .given { font-size: 24px; font-weight: 500; line-height: 1; }
  .identity .full { margin-top: 6px; line-height: 1; white-space: nowrap; }
  .identity .nick { font-size: 34px; font-weight: 700; color: var(--ink); }
  .identity .family { font-size: 26px; font-weight: 500; }
  .name-rule {
    position: absolute; left: 300px; top: 160px; width: 110px; height: 2px;
    background: linear-gradient(to right, #ffffff, var(--rule), #ffffff);
  }
  .professions {
    position: absolute;
    left: 320px;
    top: 178px;
    list-style: none;
    font-size: 15px;
    font-weight: 700;
    font-style: italic;
    color: var(--ink);
    line-height: 23px;
  }

  /* back */
  .back .band {
    position: absolute; left: 0; top: 0; width: 551px; height: 208px;
    background: var(--cyan);
    box-shadow: 0 4px 8px -2px rgba(40, 48, 46, 0.25);
  }
  .back .t-kelbro  { left: 202px; top: 30px;  width: 77px; height: 77px; background: #fff; border-radius: 10px 0 0 0; font-size: 10px; }
  .back .t-cast    { left: 279px; top: 42px;  width: 64px; height: 65px; background: #fff; border-radius: 0 12px 0 0; font-size: 9px; }
  .back .t-lantern { left: 212px; top: 107px; width: 67px; height: 71px; background: #fff; border-radius: 0 0 0 12px; font-size: 8.5px; }
  .back .t-torlen  { left: 279px; top: 107px; width: 74px; height: 77px; background: #fff; border-radius: 0 0 12px 0; font-size: 10px; }
  .back .tile .brand-dot { width: 6px; height: 6px; margin-bottom: 3px; }
  .back .grid-line-v {
    position: absolute; left: 278px; top: 24px; width: 2px; height: 166px; background: #d9dcdc;
  }
  .back .grid-line-h {
    position: absolute; left: 170px; top: 106px; width: 220px; height: 2px;
    background: linear-gradient(to right, transparent, #d9dcdc 30%, #d9dcdc 70%, transparent);
  }

  .contact {
    position: absolute; left: 0; width: 551px;
    font-size: 11px; font-weight: 500; color: var(--slate);
    display: flex; justify-content: center; align-items: center; gap: 8px;
  }
  .contact svg { width: 12px; height: 12px; fill: var(--slate); flex: none; }
  .contact.phone { top: 232px; }
  .contact.address { top: 258px; }
  .contact.online { top: 283px; gap: 6px; }
  .contact .divider { width: 1px; height: 14px; background: var(--slate); margin: 0 14px 0 12px; }
</style>
</head>
<body>
  <p class="side-label front">FRONT</p>
  <p class="side-label back">BACK</p>

  <section class="card front">
    <div class="tile shaded t-kelbro"><div class="tile-inner"><span class="brand-dot"></span>KelbroNest</div></div>
    <div class="tile shaded t-cast"><div class="tile-inner"><span class="brand-dot"></span>Drosk<br>Harbor Cast</div></div>
    <div class="tile shaded t-lantern"><div class="tile-inner"><span class="brand-dot"></span>Quiet Lantern<br>Properties</div></div>
    <div class="tile shaded t-torlen"><div class="tile-inner"><span class="brand-dot"></span>Torlen<br>Products</div></div>
    <div class="grid-line-v"></div>
    <div class="grid-line-h"></div>

    <div class="identity">
      <p class="given">Dae hwan</p>
      <p class="full"><span class="nick">RIKO</span> <span class="family">Pellow</span></p>
    </div>
    <div class="name-rule"></div>
    <ul class="professions">
      <li>Prototyping Engineer</li>
      <li>Real Estate Investor</li>
      <li>Financial Blogger</li>
      <li>Video Podcaster</li>
      <li>Online Retail Seller</li>
    </ul>
  </section>

  <section class="card back">
    <div class="band"></div>
    <div class="tile t-kelbro"><div class="tile-inner"><span class="brand-dot"></span>KelbroNest</div></div>
    <div class="tile t-cast"><div class="tile-inner"><span class="brand-dot"></span>Drosk<br>Harbor Cast</div></div>
    <div class="tile t-lantern"><div class="tile-inner"><span class="brand-dot"></span>Quiet Lantern<br>Properties</div></div>
    <div class="tile t-torlen"><div class="tile-inner"><span class="brand-dot"></span>Torlen<br>Products</div></div>
    <div class="grid-line-v"></div>
    <div class="grid-line-h"></div>

    <p class="contact phone">
      <svg viewBox="0 0 24 24" aria-hidden="true"><path d="M6.6 10.8a15.1 15.1 0 0 0 6.6 6.6l2.2-2.2a1 1 0 0 1 1-.25 11.4 11.4 0 0 0 3.6.57 1 1 0 0 1 1 1V20a1 1 0 0 1-1 1A17 17 0 0 1 3 4a1 1 0 0 1 1-1h3.5a1 1 0 0 1 1 1c0 1.25.2 2.45.57 3.57a1 1 0 0 1-.25 1z"/></svg>
      555-574-2916
    </p>
    <p class="contact address">
      <svg viewBox="0 0 24 24" aria-hidden="true"><path d="M12 2a7 7 0 0 0-7 7c0 5.25 7 13 7 13s7-7.750 7-13a7 7 0 0 0-7-7zm0 9.5A2.5 2.5 0 1 1 12 6.5a2.5 2.5 0 0 1 0 5z"/></svg>
      83 Tolmer Court, Brindlewick OR 97392
    </p>
    <p class="contact online">
      <svg viewBox="0 0 24 24" aria-hidden="true"><path d="M2 5h20v14H2zm2 2v.5l8 5 8-5V7z"/></svg>
      RikodPellow@mailnest.example
      <span class="divider"></span>
      <svg viewBox="0 0 24 24" aria-hidden="true"><path d="M5 2l14 9-6 1.5 4 7.5-2.6 1.4-4-7.6L5 18z"/></svg>
      www.kelbronest.com
    </p>
  </section>
</body>
</html>
```